Lume Hart Co Need a custom graphic

I need to have the attached chart re-designed in a hand colored pencil format. The heading needs to be changed to "The most effective methods for hiring sales people". Do not include the background logo in the sample file.

Place the attached Lume Hart Co logo next to the most effective methods (91%)

```html
<!DOCTYPE html>
<html lang="en">
<head>
<meta charset="utf-8">
<title>The Most Effective Methods for Hiring Sales People</title>
<link href="https://fonts.googleapis.com/css2?family=Bebas+Neue&family=Mouse+Memoirs&display=swap" rel="stylesheet">
<style>
  :root {
    --navy: #13265e;
    --navy-deep: #0f2158;
    --label-navy: #1b2d6b;
    --sky: #0a9ee0;
    --line-red: #e3161d;
    --dot-red: #a5121a;
    --grid: #c3c6cf;
    --stripe: #d6d9e3;
    --paper: #f6f6f3;
    --page: #ffffff;
    --white: #ffffff;
    --axis: #1a1a1a;
  }
  html, body {
    margin: 0;
    width: 1200px;
    height: 1022px;
    overflow: hidden;
    background: var(--page);
  }
  .chart-card {
    position: absolute;
    left: 108px;
    top: 112px;
    width: 984px;
    height: 761px;
    background: var(--paper);
    box-shadow: 0 10px 30px rgba(0,0,0,0.16);
  }
  .chart-card svg { display: block; }
  .headline { font-family: "Mouse Memoirs", "Bebas Neue", sans-serif; }
  .headline-top { fill: var(--sky); }
  .headline-bottom { fill: var(--white); }
  .axis-title { font-family: "Mouse Memoirs", "Bebas Neue", sans-serif; fill: var(--white); font-size: 56px; letter-spacing: 1px; }
  .tick-label { font-family: "Bebas Neue", sans-serif; font-size: 24px; fill: var(--axis); }
  .point-label { font-family: "Bebas Neue", sans-serif; font-size: 28px; fill: var(--label-navy); }
  .brand-name { font-family: "Bebas Neue", sans-serif; font-size: 58px; fill: var(--label-navy); letter-spacing: 1px; }
</style>
</head>
<body>
<div class="chart-card">
  <svg viewBox="180 187 1640 1268" width="984" height="761" aria-labelledby="chart-title">
    <defs>
      <filter id="pencil-fill" x="-5%" y="-5%" width="110%" height="110%">
        <feTurbulence type="fractalNoise" baseFrequency="0.85" numOctaves="3" seed="4" result="noise"/>
        <feDisplacementMap in="SourceGraphic" in2="noise" scale="5" xChannelSelector="R" yChannelSelector="G" result="rough"/>
        <feColorMatrix in="noise" type="matrix" values="0 0 0 0 0  0 0 0 0 0  0 0 0 0 0  0 0 0 -1.7 1.6" result="grain"/>
        <feComposite in="rough" in2="grain" operator="in"/>
      </filter>
      <filter id="pencil-line" x="-5%" y="-5%" width="110%" height="110%">
        <feTurbulence type="fractalNoise" baseFrequency="0.04 0.9" numOctaves="2" seed="7" result="wobble"/>
        <feDisplacementMap in="SourceGraphic" in2="wobble" scale="3.5" xChannelSelector="R" yChannelSelector="G" result="rough"/>
        <feTurbulence type="fractalNoise" baseFrequency="1.2" numOctaves="2" seed="2" result="speck"/>
        <feColorMatrix in="speck" type="matrix" values="0 0 0 0 0  0 0 0 0 0  0 0 0 0 0  0 0 0 -1.4 1.45" result="grain"/>
        <feComposite in="rough" in2="grain" operator="in"/>
      </filter>
      <filter id="pencil-text" x="-2%" y="-10%" width="104%" height="120%">
        <feTurbulence type="fractalNoise" baseFrequency="1.1" numOctaves="2" seed="9" result="speck"/>
        <feColorMatrix in="speck" type="matrix" values="0 0 0 0 0  0 0 0 0 0  0 0 0 0 0  0 0 0 -1.2 1.35" result="grain"/>
        <feComposite in="SourceGraphic" in2="grain" operator="in"/>
      </filter>
      <pattern id="hatch-light" width="9" height="9" patternUnits="userSpaceOnUse" patternTransform="rotate(35)">
        <line x1="0" y1="0" x2="0" y2="9" stroke="var(--white)" stroke-width="2" stroke-opacity="0.13"/>
      </pattern>
      <pattern id="hatch-stripe" width="7" height="7" patternUnits="userSpaceOnUse" patternTransform="rotate(-30)">
        <line x1="0" y1="0" x2="0" y2="7" stroke="#b9bdca" stroke-width="2.2" stroke-opacity="0.55"/>
      </pattern>
    </defs>

    <!-- header band -->
    <g class="header-band">
      <g filter="url(#pencil-fill)">
        <polygon points="180,187 180,260 350,425 380,425 200,187" fill="var(--sky)"/>
        <polygon points="1820,187 1820,260 1650,425 1620,425 1800,187" fill="var(--sky)"/>
        <polygon points="195,187 1805,187 1615,475 385,475" fill="var(--navy-deep)"/>
        <polygon points="195,187 1805,187 1615,475 385,475" fill="url(#hatch-light)"/>
      </g>
      <g filter="url(#pencil-text)">
        <text id="chart-title" class="headline headline-top" x="1000" y="335" font-size="118" text-anchor="middle" textLength="1145" lengthAdjust="spacingAndGlyphs">THE MOST EFFECTIVE METHODS</text>
        <text class="headline headline-bottom" x="1002" y="445" font-size="112" text-anchor="middle" textLength="965" lengthAdjust="spacingAndGlyphs">FOR HIRING SALES PEOPLE</text>
      </g>
    </g>

    <!-- column stripes -->
    <g class="column-stripes" filter="url(#pencil-fill)">
      <g fill="var(--stripe)" fill-opacity="0.75">
        <rect x="372" y="560" width="128" height="758"/>
        <rect x="600" y="560" width="131" height="758"/>
        <rect x="853" y="560" width="132" height="758"/>
        <rect x="1108" y="560" width="130" height="758"/>
        <rect x="1358" y="560" width="132" height="758"/>
        <rect x="1597" y="560" width="131" height="758"/>
      </g>
      <g fill="url(#hatch-stripe)">
        <rect x="372" y="560" width="128" height="758"/>
        <rect x="600" y="560" width="131" height="758"/>
        <rect x="853" y="560" width="132" height="758"/>
        <rect x="1108" y="560" width="130" height="758"/>
        <rect x="1358" y="560" width="132" height="758"/>
        <rect x="1597" y="560" width="131" height="758"/>
      </g>
    </g>

    <!-- gridlines -->
    <g class="gridlines" stroke="var(--grid)" stroke-width="1.8" filter="url(#pencil-line)">
      <line x1="372" y1="596" x2="1728" y2="596"/>
      <line x1="372" y1="677" x2="1728" y2="677"/>
      <line x1="372" y1="758" x2="1728" y2="758"/>
      <line x1="372" y1="842" x2="1728" y2="842"/>
      <line x1="372" y1="918" x2="1728" y2="918"/>
      <line x1="372" y1="1000" x2="1728" y2="1000"/>
      <line x1="372" y1="1078" x2="1728" y2="1078"/>
      <line x1="372" y1="1160" x2="1728" y2="1160"/>
      <line x1="372" y1="1241" x2="1728" y2="1241"/>
    </g>

    <!-- axes -->
    <g class="axes" stroke="var(--axis)" stroke-width="3.5" filter="url(#pencil-line)">
      <line x1="370" y1="490" x2="370" y2="1321"/>
      <line x1="369" y1="1320" x2="1728" y2="1320"/>
    </g>

    <g class="tick-labels" text-anchor="end" filter="url(#pencil-text)">
      <text class="tick-label" x="356" y="603">0.90</text>
      <text class="tick-label" x="356" y="684">0.80</text>
      <text class="tick-label" x="356" y="765">0.70</text>
      <text class="tick-label" x="356" y="849">0.60</text>
      <text class="tick-label" x="356" y="925">0.50</text>
      <text class="tick-label" x="356" y="1007">0.40</text>
      <text class="tick-label" x="356" y="1085">0.30</text>
      <text class="tick-label" x="356" y="1167">0.20</text>
      <text class="tick-label" x="356" y="1248">0.10</text>
      <text class="tick-label" x="356" y="1325">0.00</text>
    </g>

    <!-- axis titles -->
    <g class="axis-boxes" filter="url(#pencil-fill)">
      <rect x="235" y="625" width="70" height="556" rx="6" fill="var(--navy)"/>
      <rect x="235" y="625" width="70" height="556" rx="6" fill="url(#hatch-light)"/>
      <rect x="792" y="1338" width="452" height="70" rx="4" fill="var(--navy)"/>
      <rect x="792" y="1338" width="452" height="70" rx="4" fill="url(#hatch-light)"/>
    </g>
    <g filter="url(#pencil-text)">
      <text class="axis-title" transform="translate(290 903) rotate(-90)" text-anchor="middle" textLength="440" lengthAdjust="spacingAndGlyphs">PREDICTIVE VALIDITY</text>
      <text class="axis-title" x="1018" y="1392" text-anchor="middle" textLength="334" lengthAdjust="spacingAndGlyphs">HIRING METHOD</text>
    </g>

    <!-- data line -->
    <polyline class="validity-line" fill="none" stroke="var(--line-red)" stroke-width="4.5" stroke-linejoin="round" filter="url(#pencil-line)"
      points="492,1255 600,1176 737,1160 861,1161 983,1142 1108,1142 1235,1065 1358,918 1483,841 1599,743 1728,609"/>
    <g class="data-points" fill="var(--dot-red)" filter="url(#pencil-fill)">
      <circle cx="492" cy="1255" r="8"/>
      <circle cx="600" cy="1176" r="8"/>
      <circle cx="737" cy="1160" r="8"/>
      <circle cx="861" cy="1161" r="8"/>
      <circle cx="983" cy="1142" r="8"/>
      <circle cx="1108" cy="1142" r="8"/>
      <circle cx="1235" cy="1065" r="8"/>
      <circle cx="1358" cy="918" r="8"/>
      <circle cx="1483" cy="841" r="8"/>
      <circle cx="1599" cy="743" r="8"/>
      <circle cx="1728" cy="609" r="8"/>
    </g>

    <!-- point labels -->
    <g class="point-labels" filter="url(#pencil-text)">
      <text class="point-label" x="412" y="1287">CULTURE TEST, 13%</text>
      <text class="point-label" x="531" y="1162">RESUME, 18%</text>
      <text class="point-label" x="745" y="1192" text-anchor="middle">BEHAVIOR/</text>
      <text class="point-label" x="745" y="1217" text-anchor="middle">PERSONALITY TEST, 20%</text>
      <text class="point-label" x="862" y="1114" text-anchor="middle">TRADITIONAL</text>
      <text class="point-label" x="862" y="1138" text-anchor="middle">INTERVIEW, 20%</text>
      <text class="point-label" x="990" y="1186" text-anchor="middle">REFERENCE</text>
      <text class="point-label" x="990" y="1210" text-anchor="middle">CHECK, 23%</text>
      <text class="point-label" x="1165" y="1168" text-anchor="middle">EMOTIONAL</text>
      <text class="point-label" x="1165" y="1193" text-anchor="middle">INTELLIGENCE, 23%</text>
      <text class="point-label" x="1267" y="1075">SKILLS TEST, 33%</text>
      <text class="point-label" x="1345" y="914" text-anchor="end" textLength="269" lengthAdjust="spacingAndGlyphs">GENERAL MENTAL ABILITY, 51%</text>
      <text class="point-label" x="1463" y="838" text-anchor="end" textLength="477" lengthAdjust="spacingAndGlyphs">HIGHLY STRUCTURED INTERVIEW WITH SCORECARD, 57%</text>
      <text class="point-label" x="1580" y="748" text-anchor="end" textLength="354" lengthAdjust="spacingAndGlyphs">MULTI-MEASUREMENT ASSESSMENT, 71%</text>
      <text class="point-label" x="1702" y="622" text-anchor="end" textLength="495" lengthAdjust="spacingAndGlyphs">SALES-SPECIFIC MULTI-MEASUREMENT ASSESSMENT, 91%</text>
    </g>

    <!-- brand -->
    <g class="brand" filter="url(#pencil-text)">
      <text class="brand-name" x="1775" y="560" text-anchor="end" textLength="300" lengthAdjust="spacingAndGlyphs">LUME HART CO</text>
    </g>
  </svg>
</div>
</body>
</html>
```